WTF!!! We need a modern professional website for a business litigation law firm.

We need a modern, clean, professional and uncomplicated website for a new business trial and litigation law firm called "Harrowgate Trial Firm PLLC". Website must be mobile optimized for iPad and smartphone. The law firm specializes in counseling and representing large corporations, small businesses and entrepreneurs in and out of the courtroom. Lawyers in the firm serve as Florida counsel and trial counsel to organizations facing claims involving product liability, premises liability, professional liability, vehicle and transportation liability, warranty claims, construction defects and delay claims, complex business disputes, commercial litigation and bid disputes in State and Federal Courts. The website is mainly to provide information about the firm, and should include sections describing the firm, identifying the Industries Served and Areas of Practice ," a separate page identifying the "Professionals", a separate page for "Resources & Advisories," and a traveling "Connect With Us" button a site visitor can click on that will launch an email to the Firm's general email account. The website should allow us to easily modify the content on these pages, and let us add/modify links to external information sources. We will not sell anything or take payments through the website. We do need to be able to easily upload and update photographs of attorneys and add new attorneys names/email hyperlinks as the firm grows. We would like to add developments in the law or success stories easily and quickly, such as through a blog page. On the "Connect With Us" page the website should have hyperlinks to email the Firm, and there should be hyperlinks to email each professional on the "Professionals" page. The website should be viewable on mobile devices without distortion. The law firm focuses on trial work and should have some imagery associated with courtrooms, but the overall theme of the site should be modern, clean, and communicate sophistication and strength. The website should be made in Wordpress. We have uploaded logo files for Harrowgate Trial Firm.

Target Market(s)

Corporations and companies that are looking for legal representation. Other attorneys/legal industry.

Industry/Entity Type

Legal Industry

Coding

Coded - Design and coding required

Number of Pages Required

1 page

Font styles to use
Sans Serif

Requirements
Must have
• Simple, clean, sophisticated, modern website that includes the logo, watermark of logo, and the elements described above.
Nice to have
• Pictures of city scape, buildings, courtroom, team members.

```html
<!DOCTYPE html>
<html lang="en">
<head>
<meta charset="utf-8">
<title>Harrowgate Trial Firm PLLC</title>
<link href="https://fonts.googleapis.com/css2?family=Open+Sans:wght@400;600;700;800&display=swap" rel="stylesheet">
<style>
:root{
  --gold:#c69c6d;
  --gold-dark:#b58955;
  --ink:#1c1c1c;
  --dark:#161616;
  --cream:#fdf6ee;
  --text:#333;
  --muted:#7a7a7a;
  --white:#fff;
}
*{box-sizing:border-box;margin:0;padding:0}
html,body{width:1200px;height:4139px;overflow:hidden}
body{font-family:"Open Sans",sans-serif;color:var(--text);background:var(--white);position:relative}
.abs{position:absolute}
section,header,footer{position:absolute;left:0;width:1200px;overflow:hidden}
.btn{position:absolute;display:flex;align-items:center;justify-content:center;background:var(--gold);color:var(--white);border-radius:30px;font-weight:600;text-transform:uppercase;letter-spacing:.3px}
.section-title{position:absolute;left:0;width:1200px;text-align:center;font-weight:700;font-size:32px;color:var(--ink);letter-spacing:.5px}
.section-title::after{content:"";display:block;width:52px;height:4px;background:var(--gold);margin:10px auto 0}
.section-sub{position:absolute;left:0;width:1200px;text-align:center;font-size:14px;color:#555}
.slant{position:absolute;left:0;width:1200px}

/* hero */
.hero{top:0;height:740px;background:#1b1814}
.hero-photo{position:absolute;inset:0;background:linear-gradient(90deg,#14120f 0%,#221d17 40%,#3a3128 62%,#4a3d30 75%,#2a241d 100%)}
.logo-box{position:absolute;left:112px;top:0;width:169px;height:140px;background:var(--white);border-radius:0 0 26px 26px;display:flex;flex-direction:column;align-items:center;justify-content:center;gap:8px;z-index:3}
.logo-box .mark{width:34px;height:34px;background:var(--ink)}
.logo-box .name{font-weight:800;font-size:17px;color:var(--ink);text-align:center;line-height:1.15;text-transform:uppercase}
.nav{position:absolute;left:326px;top:21px;width:761px;height:58px;background:var(--white);border-radius:29px;display:flex;align-items:center;padding-left:0;overflow:hidden;z-index:3}
.nav a{font-size:13px;color:var(--ink);text-decoration:none;padding:0 11px;height:58px;display:flex;align-items:center;font-weight:600}
.nav a.active{background:var(--gold);color:var(--white);padding:0 11px 0 17px}
.hero-title{position:absolute;left:100px;width:546px;top:272px;text-align:center;color:var(--gold);font-weight:800;font-size:56px;line-height:62px;text-transform:uppercase}
.hero-text{position:absolute;left:120px;width:506px;top:412px;text-align:center;color:var(--white);font-size:14px;line-height:24px}

/* about */
.about{top:740px;height:617px;background:var(--white)}
.about-photo{position:absolute;left:112px;top:65px;width:461px;height:475px;background:linear-gradient(160deg,#c9c4bc,#8a7e70 55%,#e9e6e2)}
.dots{position:absolute;left:76px;top:488px;width:158px;height:86px;background-image:radial-gradient(#d8d8d8 2px,transparent 2.4px);background-size:10px 10px}
.about-head{position:absolute;left:655px;top:118px;border-left:4px solid var(--gold);padding-left:14px;font-size:31px;font-weight:700;color:var(--ink);height:52px;line-height:52px}
.about-lead{position:absolute;left:655px;top:185px;width:400px;font-size:14px;line-height:23px;font-weight:600;color:#333}
.about-p{position:absolute;left:655px;width:400px;font-size:13.5px;line-height:23px;color:var(--muted)}

/* practice */
.practice{top:1357px;height:603px;background:var(--cream)}
.area-icon{position:absolute;width:94px;height:94px;border:2px solid var(--gold);border-radius:50%;display:flex;align-items:center;justify-content:center;background:var(--white)}
.area-title{position:absolute;font-size:24px;font-weight:600;color:var(--ink);line-height:28px}
.area-text{position:absolute;width:310px;font-size:13.5px;line-height:23px;color:var(--muted)}

/* professionals */
.pros{top:1960px;height:674px;background:var(--dark)}
.pros .section-title{color:var(--white)}
.pro-photo{position:absolute;top:150px;width:268px;height:355px}
.pro-name{position:absolute;width:268px;text-align:center;top:524px;color:var(--white);font-size:18px;font-weight:600}
.pro-role{position:absolute;width:268px;text-align:center;top:550px;color:var(--gold);font-size:13px}
.arrow{position:absolute;top:287px;width:46px;height:46px;background:var(--white);display:flex;align-items:center;justify-content:center}

/* blog */
.blog{top:2634px;height:731px;background:var(--white)}
.blog-photo{position:absolute;top:149px;width:472px;height:336px}
.blog-title{position:absolute;top:502px;font-size:22px;font-weight:600;color:var(--ink)}
.blog-text{position:absolute;top:549px;width:460px;font-size:13.5px;line-height:24px;color:var(--muted)}

/* contact */
.contact{top:3365px;height:409px;background:var(--cream)}
.field{position:absolute;background:var(--white);border:1px solid #d9d0c4;font-size:12.5px;color:#555;padding:9px 14px}

/* footer */
.footer{top:3774px;height:365px;background:var(--dark);color:var(--white)}
.foot-name{position:absolute;left:189px;width:280px;top:62px;text-align:center;font-weight:800;font-size:38px;line-height:44px;text-transform:uppercase;color:var(--white)}
.foot-mark{position:absolute;left:299px;top:12px;width:44px;height:44px;background:var(--white)}
.social{position:absolute;top:237px;width:40px;height:40px;border:2px solid var(--white);border-radius:50%}
.social.on{background:var(--gold);border-color:var(--gold)}
.copy{position:absolute;left:181px;top:296px;font-size:14px}
.foot-head{position:absolute;top:56px;font-size:17px;font-weight:600;letter-spacing:.3px}
.info-icon{position:absolute;left:601px;width:42px;height:42px;border:1.5px solid var(--gold);border-radius:50%;display:flex;align-items:center;justify-content:center}
.info{position:absolute;left:658px;font-size:13.5px;line-height:20px}
.links{position:absolute;left:906px;top:90px;list-style:none}
.links li{font-size:14px;height:26.7px;display:flex;align-items:center;gap:14px}
.links li::before{content:"»";color:var(--gold);font-weight:700}
</style>
</head>
<body>

<header class="hero">
  <div class="hero-photo" role="img" aria-label="Senior attorney in a dark suit with arms crossed in a wood-panelled law office"></div>
  <div class="logo-box"><span class="mark"></span><span class="name">Harrowgate<br>Trial Firm</span></div>
  <nav class="nav">
    <a class="active" href="#">HOME</a><a href="#">ABOUT</a><a href="#">PRACTICE AREAS</a><a href="#">PROFESSIONALS</a><a href="#">RESOURCES &amp; ADVISORIES</a><a href="#">BLOG</a><a href="#">CONTACT US</a>
  </nav>
  <h1 class="hero-title">Harrowgate<br>Trial Firm PLLC</h1>
  <p class="hero-text">But I must explain to you how all this mistaken idea of denouncing pleasure and praising pain was born and I will give you a complete account of the actual teachings of the great explorer of the truth</p>
  <a class="btn" style="left:263px;top:511px;width:219px;height:46px;font-size:15px;font-weight:700">Connect With Us</a>
  <svg class="slant" style="top:670px" width="1200" height="70"><polygon points="0,70 1200,5 1200,70" fill="var(--gold)"/></svg>
</header>

<section class="about">
  <div class="dots"></div>
  <div class="about-photo" role="img" aria-label="Smiling attorney in a white blouse reviewing documents at her desk"></div>
  <h2 class="about-head">ABOUT US</h2>
  <p class="about-lead">Lorem ipsum dolor sit amet, consectetur adipiscing elit, seddo eiusmod tempor incididunt ut labore et dolore</p>
  <p class="about-p" style="top:254px">magna aliquaa Ut enim ad minim veniam, quis nostrud lorem exercitation ullamcon laboris nisi ut aliquip ex ea commodose consequat. Duis aute an irure dolor in reprehenderit in volupt atevelit esse cillum dolo eu fugiat nulla pariatur.</p>
  <p class="about-p" style="top:368px">It is a long established fact that a reader will be distracted by the readable content of a page when looking at its layout. The point of using Lorem Ipsum is that it has a more..</p>
  <a class="btn" style="left:655px;top:468px;width:138px;height:43px;font-size:14px">Read More</a>
</section>

<section class="practice">
  <h2 class="section-title" style="top:52px">PRACTICE AREAS</h2>
  <p class="section-sub" style="top:113px">But I must explain to you how all this mistaken idea of denouncing pleasure and praising pain was born</p>

  <div class="area-icon" style="left:112px;top:191px"><svg width="50" height="50" fill="none" stroke="var(--gold)" stroke-width="2"><circle cx="15" cy="12" r="5"/><path d="M8 44V24h14v20"/><rect x="28" y="22" width="16" height="16"/><path d="M28 28h16"/></svg></div>
  <h3 class="area-title" style="left:226px;top:200px">Product Liability</h3>
  <p class="area-text" style="left:226px;top:238px">But I must explain to you how all this mistaken idea of denouncing pleasure and praising pain was born and I will give you a complete</p>

  <div class="area-icon" style="left:655px;top:191px"><svg width="50" height="50" fill="none" stroke="var(--ink)" stroke-width="2"><path d="M25 6l10 6v11l-10 6-10-6V12z"/><path d="M6 26l8 14h8M44 26l-8 14h-8"/></svg></div>
  <h3 class="area-title" style="left:771px;top:200px">Premises Liability</h3>
  <p class="area-text" style="left:771px;top:238px">But I must explain to you how all this mistaken idea of denouncing pleasure and praising pain was born and I will give you a complete</p>

  <div class="area-icon" style="left:112px;top:356px"><svg width="50" height="50" fill="none" stroke="var(--gold)" stroke-width="2"><path d="M18 8l12 4v10c0 8-6 13-12 16-6-3-12-8-12-16V12z"/><circle cx="37" cy="14" r="4" stroke="var(--ink)"/><path d="M31 44V24h12v20" stroke="var(--ink)"/></svg></div>
  <h3 class="area-title" style="left:226px;top:365px">Professional Liability</h3>
  <p class="area-text" style="left:226px;top:403px">But I must explain to you how all this mistaken idea of denouncing pleasure and praising pain was born and I will give you a complete</p>

  <div class="area-icon" style="left:655px;top:356px"><svg width="50" height="50" fill="none" stroke="var(--gold)" stroke-width="2"><rect x="16" y="6" width="24" height="18" rx="4"/><circle cx="21" cy="20" r="2"/><circle cx="35" cy="20" r="2"/><path d="M4 36h10l8 4h14l8-8" stroke="var(--ink)"/></svg></div>
  <h3 class="area-title" style="left:771px;top:365px">Vehicle and<br>Transportation Liability</h3>
  <p class="area-text" style="left:771px;top:426px">But I must explain to you how all this mistaken idea of denouncing pleasure</p>

  <svg class="slant" style="top:533px" width="1200" height="70"><polygon points="0,0 0,70 1200,70 1200,58" fill="var(--gold)"/></svg>
</section>

<section class="pros">
  <h2 class="section-title" style="top:60px">OUR PROFESSIONALS</h2>
  <div class="arrow" style="left:53px"><svg width="20" height="12" fill="none" stroke="#222" stroke-width="1.6"><path d="M19 6H2M7 1L2 6l5 5"/></svg></div>
  <div class="arrow" style="left:1108px"><svg width="20" height="12" fill="none" stroke="#222" stroke-width="1.6"><path d="M1 6h17M13 1l5 5-5 5"/></svg></div>

  <div class="pro-photo" style="left:141px;background:linear-gradient(170deg,#cfd6d8,#5a6f8c 60%,#2d3b55)" role="img" aria-label="Attorney in a blue suit with arms crossed"></div>
  <p class="pro-name" style="left:141px">Daniel Mercer</p><p class="pro-role" style="left:141px">Attorney</p>

  <div class="pro-photo" style="left:467px;background:linear-gradient(170deg,#e2dcd2,#c99a2e 60%,#8f6d2a)" role="img" aria-label="Attorney in a mustard blazer with arms crossed"></div>
  <p class="pro-name" style="left:467px">Claire Donovan</p><p class="pro-role" style="left:467px">Attorney</p>

  <div class="pro-photo" style="left:793px;background:linear-gradient(170deg,#b49b7c,#e9e6e1 55%,#c8c2b8)" role="img" aria-label="Attorney in a white shirt and tie"></div>
  <p class="pro-name" style="left:793px">Robert Ashford</p><p class="pro-role" style="left:793px">Attorney</p>

  <svg class="slant" style="top:624px" width="1200" height="50"><polygon points="0,38 1200,0 1200,50 0,50" fill="var(--gold)"/></svg>
</section>

<section class="blog">
  <h2 class="section-title" style="top:40px">LATEST BLOG</h2>
  <p class="section-sub" style="top:100px">But I must explain to you how all this mistaken idea of denouncing pleasure and praising pain was born</p>

  <div class="blog-photo" style="left:111px;background:linear-gradient(160deg,#8a5a36,#b89a7a 45%,#e6e3df)" role="img" aria-label="Team of lawyers meeting around a laptop"></div>
  <h3 class="blog-title" style="left:111px">At vero eos et accusamus</h3>
  <p class="blog-text" style="left:111px">Magna aliquaa Ut enim ad minim veniam, quis nostrud lorem exercitat ion ullamcon laboris nisi ut aliquip ex ea commodose consequat. Duis aute an irure dolor in reprehenderit in volupt..</p>
  <a class="btn" style="left:111px;top:629px;width:125px;height:42px;font-size:14px">Read More</a>

  <div class="blog-photo" style="left:617px;background:linear-gradient(160deg,#3d2215,#6e3e24 50%,#2a1a12)" role="img" aria-label="Attorney presenting to colleagues in a wood-panelled courtroom"></div>
  <h3 class="blog-title" style="left:617px">At vero eos et accusamus</h3>
  <p class="blog-text" style="left:617px">Magna aliquaa Ut enim ad minim veniam, quis nostrud lorem exercitat ion ullamcon laboris nisi ut aliquip ex ea commodose consequat. Duis aute an irure dolor in reprehenderit in volupt..</p>
  <a class="btn" style="left:617px;top:629px;width:125px;height:42px;font-size:14px">Read More</a>
</section>

<section class="contact">
  <h2 class="section-title" style="top:40px">CONTACT US</h2>
  <div class="field" style="left:300px;top:138px;width:193px;height:35px">Name</div>
  <div class="field" style="left:504px;top:138px;width:191px;height:35px">Email</div>
  <div class="field" style="left:707px;top:138px;width:191px;height:35px">Phone</div>
  <div class="field" style="left:300px;top:183px;width:598px;height:79px">Message</div>
  <a class="btn" style="left:532px;top:289px;width:136px;height:42px;font-size:14px">Submit</a>
  <svg class="slant" style="top:337px" width="1200" height="72"><polygon points="0,0 1200,56 1200,72 0,72" fill="var(--gold)"/></svg>
</section>

<footer class="footer">
  <span class="foot-mark"></span>
  <p class="foot-name">Harrowgate<br>Trial Firm</p>
  <a class="social" style="left:261px" aria-label="Social profile"></a>
  <a class="social on" style="left:309px" aria-label="Social profile"></a>
  <a class="social" style="left:359px" aria-label="Social profile"></a>
  <p class="copy">©2025 Harrowgate Trial Firm. All rights reserved.</p>

  <h4 class="foot-head" style="left:609px">ADDRESS</h4>
  <div class="info-icon" style="top:101px"><svg width="16" height="16" fill="var(--gold)"><path d="M3 1l3 0 1 4-2 1c1 2 3 4 5 5l1-2 4 1v3c0 1-1 2-2 2C7 15 1 9 1 3c0-1 1-2 2-2z"/></svg></div>
  <p class="info" style="top:104px">PHONE NUMBER<br>+1 555-014-2290</p>
  <div class="info-icon" style="top:164px"><svg width="16" height="12" fill="var(--gold)"><path d="M0 0h16v2L8 7 0 2z"/><path d="M0 4l8 5 8-5v8H0z"/></svg></div>
  <p class="info" style="top:164px">EMAIL US<br>info@harrowgatetrial.com</p>
  <div class="info-icon" style="top:236px"><svg width="14" height="18" fill="var(--gold)"><path d="M7 0a7 7 0 0 1 7 7c0 5-7 11-7 11S0 12 0 7a7 7 0 0 1 7-7zm0 4a3 3 0 1 0 0 6 3 3 0 0 0 0-6z"/></svg></div>
  <p class="info" style="top:230px">ADDRESS<br>#125 ipsum dolor sit amet,<br>consectetur adipiscing</p>

  <h4 class="foot-head" style="left:903px">QUICK LINK</h4>
  <ul class="links">
    <li>Home</li><li>About Us</li><li>Practice Areas</li><li>Professionals</li><li>Resources &amp; Advisories</li><li>Blog</li><li>Contact Us</li>
  </ul>
</footer>

</body>
</html>
```